Truck Curtain/truck side Artwork design

Like to create a Truck Curtain design for our business. We are manufacturers & suppliers of quality air diffusion equipment. Our company logo must be incorporated along with a picture collage of various air distribution devices. Bullet point of the following: Air Conditioning Grilles, Flexible Duct, Sheetmetal Products, Accessories. Include the phrase "Manufacturers of High Quality Air Diffusion Products"

Industry/Entity Type

Construction

Colors

Designer to choose colors to be used in the design.

Requirements
Must have
• Company Logo, slogan " Manufacturers of High Quality Air Diffusion Equipment, Collage of items, brevanlomfab.com.au
Nice to have
• Bullet points of the following: Air Conditioning Grilles, Flexible Duct, Sheetmetal Products, Accessories

```html
<!DOCTYPE html>
<html lang="en">
<head>
<meta charset="utf-8">
<title>Brevanlom Industries – Truck Side Artwork</title>
<link rel="stylesheet" href="https://fonts.googleapis.com/css2?family=Montserrat:ital,wght@0,400;0,600;0,700;1,700&display=swap">
<style>
  :root{
    --navy:#012479;
    --navy-text:#1c2c78;
    --band:#262626;
    --wedge:#7c7d82;
    --tick:#8fd3f5;
    --white:#ffffff;
    --stage-edge:#86878b;
    --stage-mid:#d3d4d6;
    --product:#e9ebed;
    --product-shade:#cdd0d4;
    --rule:#55575c;
  }
  *{box-sizing:border-box;margin:0;padding:0}
  html,body{width:1200px;height:1015px;overflow:hidden}
  body{
    background:radial-gradient(ellipse at 50% 50%,var(--stage-mid) 0%,var(--stage-edge) 100%);
    font-family:"Montserrat",Arial,sans-serif;
    position:relative;
  }
  .banner{position:absolute;left:97px;width:1025px;height:410px;overflow:hidden}
  .banner--top{top:98px}
  .banner--bottom{top:546px}
  .banner__shapes{position:absolute;inset:0;width:1025px;height:410px}
  .tagline{
    position:absolute;left:0;top:348px;width:1025px;height:62px;
    display:flex;align-items:center;justify-content:center;
    color:var(--white);font-size:22px;font-weight:400;letter-spacing:.3px;white-space:nowrap;
  }
  .tagline strong{font-weight:700;margin-left:6px}
  .services{position:absolute;list-style:none;color:var(--white)}
  .services li{
    position:relative;font-size:28.5px;font-weight:700;font-style:italic;
    line-height:33.5px;padding-left:28px;white-space:nowrap;
  }
  .services li svg{position:absolute;left:0;top:8px;width:19px;height:19px}
  .brand{position:absolute;width:330px;height:50px;color:var(--navy-text);font-weight:600}
  .brand__mark{position:absolute;left:0;top:0;width:53px;height:48px;background:var(--navy);border-radius:3px}
  .brand__name{position:absolute;left:66px;top:-1px;font-size:23px;white-space:nowrap;letter-spacing:-.4px}
  .brand__rule{position:absolute;left:68px;top:44px;width:166px;height:1.5px;background:var(--rule)}
  .brand__suffix{position:absolute;left:246px;top:31px;font-size:16px;white-space:nowrap}
  .photo{position:absolute;background:linear-gradient(160deg,var(--white),var(--product) 55%,var(--product-shade))}
  .photo--round{border-radius:50%}
  .grille{
    position:absolute;background:linear-gradient(180deg,#fbfbfb,#dcdfe2);
    border:4px solid var(--white);transform:rotate(-2.2deg);
  }
  .grille--slot{background:linear-gradient(180deg,#f4f4f4 0%,#f4f4f4 20%,#2b2b2b 25%,#2b2b2b 40%,#f4f4f4 45%,#f4f4f4 60%,#2b2b2b 65%,#2b2b2b 80%,#f4f4f4 85%)}
</style>
</head>
<body>

<!-- Layout A: services left, brand right -->
<section class="banner banner--top">
  <svg class="banner__shapes" viewBox="0 0 1025 410" aria-hidden="true">
    <defs>
      <linearGradient id="lightA" x1="0" y1="0" x2="0" y2="1">
        <stop offset="0" stop-color="#e6e7ea"/><stop offset="1" stop-color="#ffffff"/>
      </linearGradient>
    </defs>
    <polygon points="559,0 1025,0 1025,348 486,348" fill="url(#lightA)"/>
    <polygon points="559,0 486,348 462,348" fill="#7c7d82"/>
    <polygon points="0,0 559,0 462,348 0,348" fill="#012479"/>
    <rect x="0" y="348" width="1025" height="62" fill="#262626"/>
  </svg>

  <ul class="services" style="left:54px;top:44px">
    <li><svg viewBox="0 0 20 20"><circle cx="10" cy="10" r="8" fill="none" stroke="#8fd3f5" stroke-width="2"/><path d="M6 10l3 3 7-8" fill="none" stroke="#8fd3f5" stroke-width="2.2"/></svg>Air Conditioning Grilles</li>
    <li><svg viewBox="0 0 20 20"><circle cx="10" cy="10" r="8" fill="none" stroke="#8fd3f5" stroke-width="2"/><path d="M6 10l3 3 7-8" fill="none" stroke="#8fd3f5" stroke-width="2.2"/></svg>Flexibile Duct</li>
    <li><svg viewBox="0 0 20 20"><circle cx="10" cy="10" r="8" fill="none" stroke="#8fd3f5" stroke-width="2"/><path d="M6 10l3 3 7-8" fill="none" stroke="#8fd3f5" stroke-width="2.2"/></svg>Sheetmetal Products &amp;</li>
    <li>Accessories</li>
  </ul>

  <div class="grille" style="left:72px;top:192px;width:332px;height:66px" role="img" aria-label="Photo of a white linear bar grille"></div>
  <div class="grille grille--slot" style="left:95px;top:256px;width:338px;height:56px" role="img" aria-label="Photo of a white linear slot diffuser"></div>

  <div class="brand" style="left:668px;top:36px">
    <span class="brand__mark"></span>
    <span class="brand__name">Brevanlom Industries</span>
    <span class="brand__rule"></span>
    <span class="brand__suffix">Pty Ltd</span>
  </div>

  <div class="photo photo--round" style="left:573px;top:110px;width:112px;height:96px" role="img" aria-label="Photo of a round jet nozzle diffuser"></div>
  <div class="photo photo--round" style="left:711px;top:110px;width:128px;height:96px" role="img" aria-label="Photo of a round drum diffuser"></div>
  <div class="photo photo--round" style="left:866px;top:110px;width:106px;height:106px" role="img" aria-label="Photo of a round louvre grille"></div>
  <div class="photo" style="left:571px;top:224px;width:108px;height:107px" role="img" aria-label="Photo of a swirl diffuser"></div>
  <div class="photo" style="left:709px;top:222px;width:112px;height:111px" role="img" aria-label="Photo of a square ceiling diffuser"></div>
  <div class="photo" style="left:858px;top:226px;width:106px;height:104px" role="img" aria-label="Photo of an egg crate return grille"></div>

  <p class="tagline">Manufacturers of<strong>HIGH QUALITY AIR DIFFUSION PRODUCTS</strong></p>
</section>

<!-- Layout B: brand left, services right -->
<section class="banner banner--bottom">
  <svg class="banner__shapes" viewBox="0 0 1025 410" aria-hidden="true">
    <defs>
      <linearGradient id="lightB" x1="0" y1="0" x2="0" y2="1">
        <stop offset="0" stop-color="#e6e7ea"/><stop offset="1" stop-color="#ffffff"/>
      </linearGradient>
    </defs>
    <polygon points="0,0 472,0 544,348 0,348" fill="url(#lightB)"/>
    <polygon points="472,0 568,348 544,348" fill="#7c7d82"/>
    <polygon points="472,0 1025,0 1025,348 568,348" fill="#012479"/>
    <rect x="0" y="348" width="1025" height="62" fill="#262626"/>
  </svg>

  <div class="brand" style="left:57px;top:36px">
    <span class="brand__mark"></span>
    <span class="brand__name">Brevanlom Industries</span>
    <span class="brand__rule"></span>
    <span class="brand__suffix">Pty Ltd</span>
  </div>

  <div class="photo photo--round" style="left:63px;top:108px;width:112px;height:98px" role="img" aria-label="Photo of a round jet nozzle diffuser"></div>
  <div class="photo photo--round" style="left:200px;top:110px;width:128px;height:96px" role="img" aria-label="Photo of a round drum diffuser"></div>
  <div class="photo photo--round" style="left:356px;top:110px;width:106px;height:106px" role="img" aria-label="Photo of a round louvre grille"></div>
  <div class="photo" style="left:60px;top:223px;width:108px;height:108px" role="img" aria-label="Photo of a swirl diffuser"></div>
  <div class="photo" style="left:201px;top:221px;width:108px;height:110px" role="img" aria-label="Photo of a square ceiling diffuser"></div>
  <div class="photo" style="left:347px;top:224px;width:104px;height:107px" role="img" aria-label="Photo of an egg crate return grille"></div>

  <ul class="services" style="left:576px;top:44px">
    <li><svg viewBox="0 0 20 20"><circle cx="10" cy="10" r="8" fill="none" stroke="#8fd3f5" stroke-width="2"/><path d="M6 10l3 3 7-8" fill="none" stroke="#8fd3f5" stroke-width="2.2"/></svg>Air Conditioning Grilles</li>
    <li><svg viewBox="0 0 20 20"><circle cx="10" cy="10" r="8" fill="none" stroke="#8fd3f5" stroke-width="2"/><path d="M6 10l3 3 7-8" fill="none" stroke="#8fd3f5" stroke-width="2.2"/></svg>Flexibile Duct</li>
    <li><svg viewBox="0 0 20 20"><circle cx="10" cy="10" r="8" fill="none" stroke="#8fd3f5" stroke-width="2"/><path d="M6 10l3 3 7-8" fill="none" stroke="#8fd3f5" stroke-width="2.2"/></svg>Sheetmetal Products &amp;</li>
    <li>Accessories</li>
  </ul>

  <div class="grille" style="left:594px;top:192px;width:332px;height:66px" role="img" aria-label="Photo of a white linear bar grille"></div>
  <div class="grille grille--slot" style="left:617px;top:256px;width:338px;height:56px" role="img" aria-label="Photo of a white linear slot diffuser"></div>

  <p class="tagline">Manufacturers of<strong>HIGH QUALITY AIR DIFFUSION PRODUCTS</strong></p>
</section>

</body>
</html>
```